Book Cover Design - Rooted Together: 7 Paths to Raise a Household that Blooms

International cover needed for the Australian (Fenwick Marlow/QRT Press 2011) non-fiction book Rooted Together: 7 Paths to Raise a Household that Blooms.

Blurb: With the birth of a baby, come other new beginnings, the birth of a mother, of a father, and of a family. With each stage of a child's growth, and with every new baby, there are more new beginnings. In older cultures and in villages around the world, parenthood was considered a rite of passage but traditions that guided parents into becoming a family have largely been lost - until now.

This ground breaking book walks a new generation of mothers and fathers through the eight steps of the modern parenthood rite of passage, from couple-connection to family-foundations, so they can prepare for and continue to grow a family that thrives.

Bio: Nora Pembridge is a relationship counsellor, parent educator and columnist for Homeward Nursery magazine. She lives in Sydney with her husband, their three gorgeous children and an itinerary of pets. This is her first book.
Updates

Thank you for your patience, I haven't ever done anything like this before and the designs submitted have helped me to be more specific in my requests. Please see the updated brief. The most important point is that I am seeking a TEXT based cover, so BOTH the TITLE and SUBTITLE should take up most of the space, the image could either be in the background with the title and subtitle overlayed, or be much smaller to fit around them. I have attached some more images to the brief, hope they help to convey the 'feel' I am after.  Thanks again!

Reason: Thank you so much for taking an interest in this project, the process has been very educational and helpful for me. While some of the stock art in the submitted designs are great, I've decided to commission a custom illustration which completely captures the meaning of Rooted Together. I will upload the illustration once it's complete for designers who are still interested to use. Thank you for your patience! Nora

Thank you all for your patience and for opening up my thinking about what I am really hoping for with this cover. I have uploaded some new tree designs and more specific instructions that I would like to be included in the cover design. I'm looking forward to seeing your creations!

With warm regards,

Nora

Target Market(s)

Couples thinking about having a baby and new parents of one or more young children.

Industry/Entity Type

Baby

Requirements
Must have
• TEXT based cover with BOTH the TITLE and SUBTITLE taking up most of the page.
Colors to match the Australian version (see attached)
Tree design bottom left (as per Trunk Treatment image attached) OR Heart Tree Design
Root design (as per one of the two images attached)
PLEASE ADD: three new shoots coming up from the ground under the tree to symbolize the children.
Nice to have
• Artistic effect to complement Australian cover.
Subtle retro feel to complement Australian cover.
Should not have
• The book is inclusive of all parents (including same-sex parents) so no images of mother/father and baby.

```html
<!DOCTYPE html>
<html lang="en">
<head>
<meta charset="utf-8">
<title>Rooted Together: 7 Paths to Raise a Household that Blooms</title>
<link rel="stylesheet" href="https://fonts.googleapis.com/css2?family=Cormorant+Garamond:wght@400&family=Sorts+Mill+Goudy:ital@0;1&family=Playfair+Display:wght@400&family=Alfa+Slab+One&family=Pinyon+Script&display=swap">
<style>
  :root {
    --sky-top: #62b8c2;
    --sky-mid: #a9d3da;
    --meadow: #a6d07c;
    --ink: #3a2a26;
    --moon: #f5eed9;
    --red: #c0342a;
    --teal: #4e9692;
    --mustard: #c9a120;
    --white: #ffffff;
  }
  html, body { margin: 0; padding: 0; overflow: hidden; }
  .cover {
    position: relative;
    width: 795px;
    height: 1200px;
    overflow: hidden;
    background: linear-gradient(180deg, var(--sky-top) 0%, var(--sky-mid) 52%, var(--meadow) 90%);
  }
  .art { position: absolute; }
  .art--branch-top {
    left: 500px; top: 0; width: 295px; height: 225px;
    background: radial-gradient(ellipse at 70% 40%, rgba(59,154,154,.75) 0%, rgba(59,154,154,.35) 55%, rgba(59,154,154,0) 75%);
  }
  .art--branch-left {
    left: 0; top: 340px; width: 300px; height: 230px;
    background: radial-gradient(ellipse at 30% 50%, rgba(78,160,170,.65) 0%, rgba(78,160,170,.3) 55%, rgba(78,160,170,0) 75%);
  }
  .art--sprouts {
    left: 30px; top: 1000px; width: 240px; height: 200px;
    background: radial-gradient(ellipse at 45% 60%, rgba(122,180,58,.85) 0%, rgba(122,180,58,.4) 55%, rgba(122,180,58,0) 75%);
  }
  .moon {
    position: absolute; left: 284px; top: 189px;
    width: 462px; height: 462px; border-radius: 50%;
    background: var(--moon);
  }
  .author {
    position: absolute; left: 0; top: 28px; width: 795px;
    text-align: center; margin: 0;
    font: 400 74px/1 "Cormorant Garamond", serif;
    letter-spacing: 6px; color: var(--white);
  }
  .title-rooted {
    position: absolute; left: 44px; top: 128px; margin: 0;
    font: italic 400 238px/1 "Sorts Mill Goudy", serif;
    color: var(--ink);
  }
  .title-together {
    position: absolute; left: 352px; top: 338px; width: 640px;
    margin: 0; white-space: nowrap;
    font: 400 160px/1 "Playfair Display", serif;
    color: var(--red);
    transform: scaleX(0.52); transform-origin: left top;
  }
  .rules { position: absolute; left: 384px; top: 556px; }
  .numeral { position: absolute; left: 58px; top: 528px; }
  .steps { position: absolute; left: 334px; top: 688px; width: 420px; height: 112px; }
  .step {
    position: absolute; width: 84px; height: 70px;
    background: var(--mustard);
    display: flex; align-items: center; justify-content: center;
    font: 400 34px/1 "Alfa Slab One", serif; color: var(--white);
  }
  .step--low { top: 42px; }
  .step--high { top: 0; height: 84px; align-items: flex-start; padding-top: 10px; box-sizing: border-box; }
  .heart { position: absolute; left: 432px; top: 812px; }
  .word-to {
    position: absolute; left: 524px; top: 806px; margin: 0;
    font: 400 104px/1 "Sorts Mill Goudy", serif; color: var(--ink);
  }
  .word-raise {
    position: absolute; left: 52px; top: 838px; margin: 0;
    font: 400 170px/1 "Sorts Mill Goudy", serif; color: var(--teal);
    letter-spacing: -3px;
  }
  .phrase {
    position: absolute; left: 392px; top: 932px; margin: 0;
    font: 400 50px/1 "Sorts Mill Goudy", serif; color: var(--ink);
    letter-spacing: 1px;
  }
  .phrase em { font-style: italic; }
  .word-blooms {
    position: absolute; left: 240px; top: 994px; margin: 0;
    font: 400 160px/1 "Pinyon Script", cursive; color: var(--ink);
  }
</style>
</head>
<body>
<main class="cover">
  <div class="art art--branch-top" role="img" aria-label="Teal leafy tree branch reaching in from the top right"></div>
  <div class="art art--branch-left" role="img" aria-label="Soft blue leafy branch reaching in from the left"></div>
  <div class="art art--sprouts" role="img" aria-label="Green young shoots growing up from the bottom left"></div>

  <div class="moon"></div>

  <p class="author">NORA PEMBRIDGE</p>
  <h1 class="title-rooted">Rooted</h1>
  <p class="title-together">Together:</p>

  <svg class="rules" width="204" height="36" viewBox="0 0 204 36" aria-hidden="true">
    <rect x="0" y="0" width="204" height="7" fill="var(--ink)"/>
    <rect x="0" y="16" width="204" height="2" fill="var(--ink)"/>
    <rect x="0" y="27" width="204" height="7" fill="var(--ink)"/>
  </svg>

  <svg class="numeral" width="256" height="294" viewBox="0 0 256 294" role="img" aria-label="7">
    <path d="M8 8 H248 V78 L146 286 H46 L148 88 H8 Z"
          fill="none" stroke="var(--white)" stroke-width="5" stroke-dasharray="0.1 12"
          stroke-linecap="round" stroke-linejoin="round"/>
    <path d="M22 22 H234 V74 L136 272 H68 L170 74 H22 Z"
          fill="none" stroke="var(--white)" stroke-width="4" stroke-linejoin="round"/>
    <path d="M34 34 H222 V70 L128 260 H86"
          fill="none" stroke="var(--white)" stroke-width="2" stroke-linejoin="round"/>
  </svg>

  <div class="steps" aria-label="paths">
    <span class="step step--low" style="left:0">p</span>
    <span class="step step--high" style="left:82px">a</span>
    <span class="step step--low" style="left:164px">t</span>
    <span class="step step--high" style="left:246px">h</span>
    <span class="step step--low" style="left:328px">s</span>
  </div>

  <svg class="heart" width="90" height="86" viewBox="0 0 90 86" aria-hidden="true">
    <path d="M45 80 C20 60 4 46 4 28 C4 14 15 4 28 4 C36 4 42 9 45 15 C48 9 54 4 62 4 C75 4 86 14 86 28 C86 46 70 60 45 80 Z"
          fill="none" stroke="var(--red)" stroke-width="1.5" stroke-dasharray="4 3"/>
    <path d="M45 72 C24 55 11 44 11 29 C11 18 19 10 29 10 C36 10 41 14 45 20 C49 14 54 10 61 10 C71 10 79 18 79 29 C79 44 66 55 45 72 Z"
          fill="var(--red)"/>
  </svg>

  <p class="word-to">to</p>
  <p class="word-raise">Raise</p>
  <p class="phrase"><em>a Household</em> that</p>
  <p class="word-blooms">Blooms</p>
</main>
</body>
</html>
```